Word Template for KESTREL Polls

KESTREL Polls stands for 'Kinship Evaluation Study Tracking Regional Everyday Lives Polls'. It is a collaborative research effort to format and combine multiple sources of public opinion data from around the world into merged datasets. We need a Microsoft Word template design for our research reports, dataset codebooks, crowdsourced development guidelines, and other documents that will be produced as part of the research and development. The template should match the website design and logo, which are attached to this contest (these are the files from previous successful design contests).

The main purpose will be to write reports discussing research and analysis. There will be lots data visualizations (bar charts, scatter plots, pie charts, histograms, trend line charts etc.) as well as tables, diargams, and photos mixed in wit all the text. A second purpose will be to write guidebooks to describe processes and teach others how to manage data, find variables, and write code, which will include screenshots and Word are diagrams and figures.

There are some document uploaded as examples for the kinds of things for which we need the template (working papers, codebooks, pamphlets, etc)

Target Market(s)

academia, government, non-profits, postgraduates, researchers

Font styles to use
Serif

Colors

Designer to choose colors to be used in the design.

Requirements
Must have
• A4 size page template
• Cover page
• Must match website design and logo (see attached)
Nice to have
• Colors to match logo and website (see attached)

```html
<!DOCTYPE html>
<html lang="en">
<head>
<meta charset="utf-8">
<title>KESTREL Polls – Report Template Pages</title>
<link href="https://fonts.googleapis.com/css2?family=Open+Sans:wght@400;600;700&display=swap" rel="stylesheet">
<style>
:root{
  --blue:#1a74c4;
  --blue-dark:#135fa6;
  --blue-light:#d6e8f7;
  --blue-pale:#eaf3fb;
  --ink:#3a3a3a;
  --muted:#777;
  --backdrop:#c9c9c9;
  --paper:#ffffff;
}
*{box-sizing:border-box;margin:0;padding:0}
html,body{width:1200px;height:1200px;overflow:hidden;background:var(--backdrop)}
body{position:relative;font-family:'Open Sans',sans-serif;color:var(--ink)}
.page{position:absolute;width:250px;height:354px;background:var(--paper);box-shadow:0 1px 3px rgba(0,0,0,.25);overflow:hidden}
.head{position:absolute;top:23px;left:0;display:flex;align-items:center}
.head::before{content:"";display:block;width:22px;height:6px;background:var(--blue)}
.head span{margin-left:6px;font-size:9px;letter-spacing:.2px;color:#333;text-transform:uppercase}
.body{position:absolute;left:28px;right:20px;top:46px;font-size:3.6px;line-height:5.3px;color:#555}
.body p{margin-bottom:4.5px}
.body .lead{color:var(--blue)}
.body .center{text-align:center;padding:0 20px}
.body h3{font-size:6.6px;line-height:8px;font-weight:600;color:#333;margin:3px 0 1px}
.body h4{font-size:5.6px;line-height:7px;font-weight:600;color:#333;margin:3px 0 1px}
.body .sub{font-size:3.6px;color:var(--blue)}
.foot{position:absolute;left:14px;right:14px;bottom:13px;display:flex;align-items:center}
.brand{font-size:5px;font-weight:600;color:var(--blue);white-space:nowrap;display:flex;align-items:center}
.brand i{display:inline-block;width:5px;height:5px;border-radius:50%;background:var(--blue);margin-right:2px}
.foot .rule{flex:1;height:.5px;background:var(--blue-light);margin:0 4px}
.num{width:9px;height:9px;border-radius:50%;background:var(--blue);color:#fff;font-size:4px;font-weight:700;display:flex;align-items:center;justify-content:center}
/* cover */
.cover-brand{position:absolute;top:52px;left:0;right:0;text-align:center;font-size:17px;color:var(--blue);font-weight:600}
.band{position:absolute;left:0;right:0;background:var(--blue)}
.cover .band{top:124px;height:115px}
.cover-title{position:absolute;left:70px;top:46px;color:#fff;font-weight:700;font-size:11.5px;line-height:14px}
.cover-sub{position:absolute;top:260px;left:0;right:0;text-align:center;font-size:5.5px;font-weight:600;color:var(--blue)}
/* copyright */
.legal{position:absolute;left:46px;top:298px;border-left:.7px solid var(--blue);padding-left:6px;font-size:3.4px;line-height:4.8px;color:#666;width:180px}
.legal .sub{color:var(--blue)}
/* toc */
.toc-title{font-size:7px;font-weight:600;color:var(--blue);margin:9px 0 8px}
.toc li{list-style:none;display:flex;font-size:3.7px;line-height:8.4px;color:#444}
.toc li .dots{flex:1;border-bottom:.5px dotted #999;margin:0 3px 2.6px}
/* vision box */
.callout{display:flex;align-items:center;background:var(--blue);color:#fff;padding:3px 4px;margin-bottom:6px;font-size:4px;line-height:5px}
.callout svg{flex:none;margin-right:6px}
/* tables */
table{border-collapse:separate;border-spacing:1px;width:100%;font-size:3.4px}
th{background:var(--blue);color:#fff;font-weight:600;height:6px}
td{background:var(--blue-pale);height:6.6px;padding:0 4px}
td.r{text-align:center}
tr.tot td{background:#e2e2e2;font-weight:700}
tr.phase td{background:var(--blue-light);color:var(--blue-dark)}
tr.grand td{background:var(--blue);color:#fff}
/* ruled table */
.ruled{position:absolute;left:27px;top:50px;width:201px}
.ruled .hdr{display:flex;background:var(--blue);color:#fff;font-size:5px;height:8px;align-items:center}
.ruled .hdr span{flex:1;padding-left:11px}
.ruled .row{height:9.1px;border-bottom:.5px solid var(--blue-light);border-left:.5px solid var(--blue-light);border-right:.5px solid var(--blue-light);display:flex}
.ruled .row::after{content:"";margin-left:124px;border-left:.5px solid var(--blue-light)}
/* photos */
.photo{position:absolute;background:linear-gradient(135deg,#3a2a22 0%,#6b5a4d 45%,#c7a27a 100%)}
/* thank you */
.thanks .band{top:124px;height:114px}
.thanks-title{position:absolute;left:52px;top:49px;color:#fff;font-size:13px;font-weight:700}
.contact{position:absolute;left:26px;right:10px;bottom:26px;display:flex;align-items:center;font-size:3.2px;line-height:4.4px;color:#555}
.contact .brand{font-size:7px}
.contact .brand i{width:7px;height:7px}
.contact .sep{width:.6px;height:18px;background:var(--blue);margin:0 6px}
.contact .ic{display:flex;align-items:center;gap:2px}
.contact .ic b{display:inline-block;width:3px;height:3px;border-radius:50%;background:var(--blue)}
</style>
</head>
<body>

<!-- Row 1 -->
<section class="page cover" style="left:38px;top:39px">
  <div class="cover-brand">KESTREL Polls</div>
  <div class="band"><div class="cover-title">LOREM IPSUM IS SIMPLY<br>DUMMY HAS BEEN</div></div>
  <div class="cover-sub">LOREM IPSUM IS SIMPLY DUMMY HAS BEEN</div>
</section>

<section class="page" style="left:333px;top:39px">
  <div class="legal">
    <p class="sub">Copyright © 2018 Northmere Pty Limited<br>All Rights Reserved</p>
    <p style="margin-top:4px">No part of the contents of this document may be reproduced or distributed in any form or by any means without the prior written permission of Northmere Pty Limited</p>
  </div>
</section>

<section class="page" style="left:622px;top:39px">
  <div class="head"><span>Table of Contents</span></div>
  <div class="body">
    <div class="toc-title">Contents</div>
    <ul class="toc">
      <li>Table of Contents<span class="dots"></span>01</li>
      <li>Executive Summary<span class="dots"></span>02</li>
      <li>Our Understanding of Your Needs<span class="dots"></span>02</li>
      <li>Our Recommendations<span class="dots"></span>03</li>
      <li>Our Approach<span class="dots"></span>05</li>
      <li>Budget and Timeframe<span class="dots"></span>07</li>
      <li>Appendix A: About the Team<span class="dots"></span>10</li>
      <li>Appendix B: Selected Client List<span class="dots"></span>10</li>
      <li>Appendix C: Our Capabilities<span class="dots"></span>11</li>
      <li>Appendix D: Our Process<span class="dots"></span>12</li>
    </ul>
  </div>
  <div class="foot"><span class="brand"><i></i>KESTREL Polls</span><span class="rule"></span><span class="num">01</span></div>
</section>

<section class="page" style="left:907px;top:39px">
  <div class="head"><span>Vision</span></div>
  <div class="body" style="left:26px">
    <div class="callout">
      <svg width="20" height="20" viewBox="0 0 20 20"><rect width="20" height="20" fill="#fff"/><circle cx="10" cy="10" r="7" fill="none" stroke="#1a74c4" stroke-width="1.4"/><circle cx="10" cy="10" r="4" fill="none" stroke="#1a74c4" stroke-width="1.4"/><circle cx="10" cy="10" r="1.4" fill="#1a74c4"/></svg>
      <span>TallyLeaf's mission is to help and support the self-employed and small business owners with their administrative tasks so they can focus on what matters -- their business.</span>
    </div>
    <p class="lead">Administrative tasks are cumbersome, time-consuming and often prevent small owners from focusing their time and energy on their business and their customers. They can also be extremely stressful for those attempting these tasks for the first time.</p>
    <p class="center">At TallyLeaf, we envisage accounting for the self-employed and small business owners as being <span class="lead">automated and decentralized</span></p>
    <p>Accounting can and should be done automatically. By connecting to all sources of accounting data such as bank accounts, payment systems, e-commerce websites, and invoicing systems, TallyLeaf AI automatically completes these tasks, which would take hours to do manually. Financial statements are available within a couple of clicks, and after analysing your data, TallyLeaf AI will offer you tips to improve your financial stability.</p>
    <p>What may seem like a pipedream to the millions of self-employed who struggle with their admin, is already a reality. Now is the time to join TallyLeaf on its mission to transform the world of bookkeeping through the power of AI.</p>
    <h4>The TallyLeaf model</h4>
    <p>TallyLeaf is based on an innovative license model that uses Token-as-a-License (TaaL). The token represents lifelong software license for TallyLeaf solutions. The Pre-ICO token sales will enable TallyLeaf to complete its development of TallyLeaf AI to deliver fully automatic bookkeeping.</p>
    <p>The Pre-ICO token sale will also pave the way for a future TallyLeaf ICO. TallyLeaf will launch accounting on the blockchain and ensure your accounting data is comprehensive and private, but available everywhere within your preferred apps. It will empower you to manage your data as you see fit in a fully decentralized way. Furthermore, a new range of business apps will connect to TallyLeaf to provide you with leading edge business data access to ensure you have the best available data at your fingertips.</p>
    <p>TallyLeaf supports strong data ownership laws that truly protect individuals and ensure they have complete ownership of their data. Through decentralisation TallyLeaf helps to ensure you always have full ownership of your data to decide how it should be used.</p>
    <p>To find out more about the TallyLeaf AI project, and the TallyLeaf TaaL or if you are interested in purchasing TallyLeaf TaaL, please register with your email at <u class="lead">https://www.tallyleaf.example/ico</u> so we</p>
  </div>
  <div class="foot"><span class="brand"><i></i>KESTREL Polls</span><span class="rule"></span><span class="num">03</span></div>
</section>

<!-- Row 2 -->
<section class="page" style="left:38px;top:429px">
  <div class="head"><span>Headline Here</span></div>
  <svg style="position:absolute;left:40px;top:57px" width="170" height="102" viewBox="0 0 170 102" role="img" aria-label="Monthly bar chart">
    <g font-family="Open Sans, sans-serif" font-size="3.4" fill="#666" text-anchor="middle">
      <line x1="6" y1="0" x2="6" y2="92" stroke="#aaa" stroke-width=".4"/>
      <line x1="6" y1="92" x2="163" y2="92" stroke="#aaa" stroke-width=".4"/>
      <g fill="#1a74c4">
        <rect x="8" y="31" width="11.5" height="61"/><rect x="20.5" y="18" width="11.5" height="74"/>
        <rect x="33" y="43" width="11.5" height="49"/><rect x="45.5" y="65" width="11.5" height="27"/>
        <rect x="58" y="86.5" width="11.5" height="5.5"/><rect x="70.5" y="66" width="11.5" height="26"/>
        <rect x="83" y="81.5" width="11.5" height="10.5"/><rect x="95.5" y="68.5" width="11.5" height="23.5"/>
        <rect x="108" y="64" width="11.5" height="28"/><rect x="120.5" y="36.5" width="11.5" height="55.5"/>
        <rect x="133" y="26.5" width="11.5" height="65.5"/><rect x="145.5" y="11" width="11.5" height="81"/>
      </g>
      <text x="14" y="29">120</text><text x="26" y="16">146</text><text x="39" y="41">96</text><text x="51" y="63">53</text>
      <text x="64" y="84.5">11</text><text x="76" y="64">50.5</text><text x="89" y="79.5">20.9</text><text x="101" y="66.5">46</text>
      <text x="114" y="62">55</text><text x="126" y="34.5">109</text><text x="139" y="24.5">129</text><text x="151" y="9">159</text>
      <text x="14" y="97">Jan</text><text x="26" y="97">Febr</text><text x="39" y="97">March</text><text x="51" y="97">April</text>
      <text x="64" y="97">May</text><text x="76" y="97">Jun</text><text x="89" y="97">July</text><text x="101" y="97">Aug</text>
      <text x="114" y="97">Sep</text><text x="126" y="97">Oct</text><text x="139" y="97">Nov</text><text x="151" y="97">Dec</text>
    </g>
  </svg>
  <div class="body" style="top:176px">
    <p class="lead">Administrative tasks are cumbersome, time-consuming and often prevent small owners from focusing their time and energy on their business and their customers. They can also be extremely stressful and nerve-wracking for those attempting these tasks for the first time.</p>
    <p class="center">At TallyLeaf, we envisage accounting for the self-employed and small business owners as being <span class="lead">automated and decentralized</span></p>
    <p>Accounting can and should be done automatically. By connecting to all sources of accounting data such as bank accounts, payment systems, e-commerce websites, and invoicing systems, TallyLeaf AI automatically completes these tasks, which would take hours to do manually. Financial statements are available within a couple of clicks, and after analysing your data, TallyLeaf AI will offer you tips to improve your financial stability.</p>
    <p>What may seem like a pipedream to the millions of self-employed who struggle with their admin, is already a reality. Now is the time to join TallyLeaf on its mission to transform the world of bookkeeping through the power of AI.</p>
    <h3>The TallyLeaf model</h3>
    <p>TallyLeaf is based on an innovative license model that uses Token-as-a-License (TaaL). The token represents lifelong software license for TallyLeaf solutions. The Pre-ICO token sales will enable TallyLeaf to complete its development of TallyLeaf AI to deliver fully automatic bookkeeping.</p>
    <p>The Pre-ICO token sale will also pave the way for a future TallyLeaf ICO. TallyLeaf will launch</p>
  </div>
  <div class="foot"><span class="brand"><i></i>KESTREL Polls</span><span class="rule"></span><span class="num">09</span></div>
</section>

<section class="page" style="left:333px;top:429px">
  <div class="head"><span>Budget and Timeframe</span></div>
  <div class="body">
    <h4>Implementation Estimate</h4>
    <p>The bulk of the implementation costs will be defined by discovery. Based on similar CRM implementation projects, we feel we can expect the CRM side will be somewhere between 200 and 300 hours, give or take. The wide swing in hours in phase one is related to the under-defined nature of both the integration needs and our role in the integration project. Our focus in discovery (as mentioned above) will be to nail down finalize those requirements and our role as it relates to what is needed to integrate the sites with the CRM.</p>
    <table>
      <tr><th>Task</th><th style="width:48px">Hours</th><th style="width:48px">Cost</th></tr>
      <tr><td>Discovery</td><td class="r">40</td><td class="r">$8,000</td></tr>
      <tr class="phase"><td colspan="3">Phase 1</td></tr>
      <tr><td>Discovery</td><td class="r">20-40</td><td class="r">$8,000</td></tr>
      <tr><td>Discovery</td><td class="r">20-40</td><td class="r">$8,000</td></tr>
      <tr><td>Discovery</td><td class="r">20-40</td><td class="r">$8,000</td></tr>
      <tr class="tot"><td>Total Phase 1</td><td class="r">80-240</td><td class="r">$16,800-40,000</td></tr>
      <tr class="phase"><td colspan="3">Phase 2</td></tr>
      <tr><td>Discovery</td><td class="r">20-40</td><td class="r">$8,000</td></tr>
      <tr class="tot"><td>Total Phase 2</td><td class="r">80-240</td><td class="r">$16,800-40,000</td></tr>
      <tr class="grand"><td>Total Estimated Implementation Cost</td><td class="r">220-480</td><td class="r">$44,000-96,000</td></tr>
    </table>
    <h4 style="margin-top:12px">Project Timeline</h4>
    <p>Based on the information we have out our disposal, the March launch date doesn't seem a realistic goal to get both the work done needed to provide the foundation for the future CRM instance and the integration given the state of apparent flux of the requirements. That said, we feel it prudent to proceed with discovery before committing to or pushing that date. We are currently estimating that the first phase will take somewhere between 7 and 12 weeks (including discovery) to complete.</p>
    <table>
      <tr><th>Task</th><th style="width:70px">Weeks to Complete</th></tr>
      <tr><td>Discovery</td><td class="r">1-2</td></tr>
      <tr><td>Phase 1</td><td class="r">6-10</td></tr>
      <tr><td>Phase 2</td><td class="r">8-12</td></tr>
      <tr class="tot"><td>Total Number of Weeks</td><td class="r"></td></tr>
    </table>
  </div>
  <div class="foot"><span class="brand"><i></i>KESTREL Polls</span><span class="rule"></span><span class="num">04</span></div>
</section>

<section class="page" style="left:622px;top:429px">
  <div class="head"><span>Headline Here</span></div>
  <div class="body">
    <h4 style="margin-top:4px">Solution</h4>
    <p><span class="sub">AI automated accounting</span><br>TallyLeaf builds automation in stages on top of its current system to reach full automation thanks to the TallyLeaf AI. TallyLeaf AI automates every manual task performed by the user. It starts by connecting to all sources of accounting data such as bank accounts, credit card, webshop or document management systems. Based on these data, TallyLeaf AI creates bookings and generates financial reports. Finally, TallyLeaf AI features chat-like interface that allows users to communicate seamlessly with it, viewing it as a trusted advisor over time for all their accounting queries.</p>
    <p><span class="sub">Blockchain software license or Token-as-a-License (TaaL)</span><br>It is possible to create tokens on blockchain that represent software licenses, also known as Token-as-a-Licence (TaaL). TallyLeaf creates TaaL by using the Vantix official wallet which interacts with the Vantix blockchain. Upon purchase of TaaL, the token holder is free to transfer or sell TaaL using secondary market that is built directly over the blockchain, in our case, the Vantix marketplace. TallyLeaf checks the validity of a token against the blockchain ensuring that token holders have access to the software. TaaL make distribution and securisation of software licenses easier for software developers. It also makes the management and resale of software license easier for software owners. All in all, TaaL has a higher value as a normal software license.</p>
    <h4>Pre-ICO Token sale</h4>
    <p>To realize this innovative vision, TallyLeaf is launching a pre-ICO in form of a token sale on Vantix blockchain. 20,000,000 tokens are available to purchase for the price of CHF 0.10 each during a 30-day period to be announced. Tokens represent TallyLeaf lifelong software licenses and by purchasing enough tokens, holders gain access to TallyLeaf software. 15,000 tokens give access to TallyLeaf invoicing or accounting. 20,000 tokens give access to both TallyLeaf accounting and invoicing. Future customers will still have the opportunity to buy directly yearly or monthly subscriptions to have access to TallyLeaf.</p>
    <h4>Future plans</h4>
    <p>A future ICO is planned between 18 and 24 months after the pre-ICO token sale. This offering will support the development of TallyLeaf into a fully decentralized, privacy-focused ecosystem of applications. The new model will reward each participant so that a new world with zero administrative tasks becomes reality.</p>
  </div>
  <div class="foot"><span class="brand"><i></i>KESTREL Polls</span><span class="rule"></span><span class="num">02</span></div>
</section>

<section class="page" style="left:907px;top:429px">
  <div class="head"><span>Our Understanding of Your Needs</span></div>
  <div class="body">
    <p>In the last two weeks of January 2014 we conducted high level conversations both with your staff and your technology partner Relay Studio. As a result of those conversations we've been able to gather the following high level goals for your project:</p>
    <p style="font-size:5.6px;line-height:7px;color:#888">CloudLedger must be in place to support Beacon Hall at launch and as the program evolves</p>
    <p class="lead" style="font-weight:600">The most critical aspect of this implementation both in terms of time sensitivity as well as functionality is centered around the support for the Beacon Hall project. Our current understanding of this project and how it relates to CloudLedger is as follows:</p>
    <p>■ Beacon Hall will be comprised of a series of websites focused on organizing institutions and individuals within six specific community sectors with the goal of increased institutional and public support to help the nation become better prepared to minimize the risks and maximize opportunities of changing climate.<br>■ The primary goals of the CRM application are:</p>
    <p class="lead" style="padding-left:8px">▸ capture information of individuals and organizations (along with their respective roles)<br>▸ track their progress on their site specific to-do lists and site interactions<br>▸ allow greenNation to push out next steps (ideally in an automated style) related to their to-do list progress and online interactions<br>▸ infuse greenNation's online and offline marketing program with useful segmentation information<br>▸ natively integrate with both the Beacon Hall family of sites as well as greenNation's email service provider of choice</p>
    <p>■ The data architecture must be well defined but flexible to support the core needs of the sites as launch as well as anticipated needs in the future.</p>
    <p class="lead" style="padding-left:8px">▸ For instance, the faith based site may collect a "denomination" field, while other sites may not collect that field.<br>▸ Future interactions outside of the to-do list may become necessary to track and greenNation will need a systemic way to capture those interactions, be able to segment on them and potentially provide automated marketing around those similar to the to-do list</p>
    <p>■ The information collected from the Beacon Hall sites must be combined with current information held within greenNation and provide a holistic view of institutions and individuals.</p>
  </div>
  <div class="foot"><span class="brand"><i></i>KESTREL Polls</span><span class="rule"></span><span class="num">05</span></div>
</section>

<!-- Row 3 -->
<section class="page" style="left:38px;top:810px">
  <div class="head"><span>Headline Here</span></div>
  <div class="ruled">
    <div class="hdr"><span>Lorem ipsum</span><span>Lorem ipsum</span></div>
    <div class="row"></div><div class="row"></div><div class="row"></div><div class="row"></div><div class="row"></div>
    <div class="row"></div><div class="row"></div><div class="row"></div><div class="row"></div><div class="row"></div>
    <div class="row"></div><div class="row"></div><div class="row"></div><div class="row"></div><div class="row"></div>
    <div class="row"></div><div class="row"></div><div class="row"></div><div class="row"></div><div class="row"></div>
    <div class="row"></div><div class="row"></div><div class="row"></div><div class="row"></div><div class="row"></div>
    <div class="row"></div><div class="row"></div><div class="row"></div><div class="row"></div>
  </div>
  <div class="foot"><span class="brand"><i></i>KESTREL Polls</span><span class="rule"></span><span class="num">08</span></div>
</section>

<section class="page" style="left:333px;top:810px">
  <div class="head"><span>Headline Here</span></div>
  <div class="photo" style="left:28px;top:45px;width:85px;height:131px" role="img" aria-label="Photo of a stressed businessman at a desk holding his head"></div>
  <div class="photo" style="left:28px;top:200px;width:85px;height:116px" role="img" aria-label="Photo of a businessman leaning over a table with a laptop"></div>
  <div class="body" style="left:125px;right:20px;top:45px">
    <p class="lead">TallyLeaf's mission is to help and support the self-employed and small business owners with their administrative tasks so they can focus on what matters -- their business.</p>
    <p>Administrative tasks are cumbersome, time-consuming and often prevent small owners from focusing their time and energy on their business and their customers. They can also be extremely stressful and nerve-wracking for those attempting these tasks for the first time.</p>
    <p>At TallyLeaf, we envisage accounting for the self-employed and small business owners as being <span class="lead">automated and decentralized</span></p>
    <p>Accounting can and should be done automatically. By connecting to all sources of accounting data such as bank accounts, payment systems, e-commerce websites, and invoicing systems, TallyLeaf AI automatically completes these tasks, which would take hours to do manually. Financial statements are available within a couple of clicks, and after analysing your data, TallyLeaf AI will offer you tips to improve your financial stability.</p>
    <p>What may seem like a pipedream to the millions of self-employed who struggle with</p>
    <h4 style="color:var(--blue)">The TallyLeaf model</h4>
    <p>TallyLeaf is based on an innovative license model that uses Token-as-a-License (TaaL). The token represents lifelong software license for TallyLeaf solutions. The Pre-ICO token sales will enable TallyLeaf to complete its development of TallyLeaf AI to deliver fully automatic bookkeeping.</p>
  </div>
  <div class="foot"><span class="brand"><i></i>KESTREL Polls</span><span class="rule"></span><span class="num">07</span></div>
</section>

<section class="page" style="left:622px;top:810px">
  <div class="head"><span>Headline Here</span></div>
  <div class="photo" style="left:28px;top:45px;width:201px;height:88px" role="img" aria-label="Photo of a stressed businessman at a desk holding his head"></div>
  <div class="body" style="top:140px">
    <p class="lead">TallyLeaf's mission is to help and support the self-employed and small business owners with their administrative tasks so they can focus on what matters -- their business.</p>
    <p>Administrative tasks are cumbersome, time-consuming and often prevent small owners from focusing their time and energy on their business and their customers. They can also be extremely stressful and nerve-wracking for those attempting these tasks for the first time.</p>
    <p>At TallyLeaf, we envisage accounting for the self-employed and small business owners as being <span class="lead">automated and decentralized</span></p>
    <p>Accounting can and should be done automatically. By connecting to all sources of accounting data such as bank accounts, payment systems, e-commerce websites, and invoicing systems, TallyLeaf AI automatically completes these tasks, which would take hours to do manually. Financial statements are available within a couple of clicks, and after analysing your data, TallyLeaf AI will offer you tips to improve your financial stability.</p>
    <p>What may seem like a pipedream to the millions of self-employed who struggle with their admin, is already a reality. Now is the time to join TallyLeaf on its mission to transform the world of bookkeeping through the power of AI.</p>
    <h3>The TallyLeaf model</h3>
    <p>TallyLeaf is based on an innovative license model that uses Token-as-a-License (TaaL). The token represents lifelong software license for TallyLeaf solutions. The Pre-ICO token sales will enable TallyLeaf to complete its development of TallyLeaf AI to deliver fully automatic bookkeeping.</p>
    <p>with leading edge business data access to ensure you have the best available data at your fingertips.</p>
  </div>
  <div class="foot"><span class="brand"><i></i>KESTREL Polls</span><span class="rule"></span><span class="num">06</span></div>
</section>

<section class="page thanks" style="left:907px;top:810px">
  <div class="band"><div class="thanks-title">THANK YOU</div></div>
  <div class="contact">
    <span class="brand"><i></i>KESTREL Polls</span>
    <span class="sep"></span>
    <div>
      <div class="ic"><b></b>555-0187 Ext 210</div>
      <div class="ic"><b></b>hello@kestrelpolls.example</div>
      <div class="ic"><b></b>www.kestrelpolls.example</div>
    </div>
    <div style="margin-left:6px">Unit 7, 48 Harbour Row<br>Eastport, Bay Province 4821</div>
  </div>
</section>

</body>
</html>
```